CD Cover Design Project

Don't have a huge brief or visual idea of exactly what i want, but here are the details:

Band Name: The Brinewalkers
Title: Nearly Every Road Back Home
Genre: indie rock - think Painted In Tunnels, Marrow, Pemby, The Torvals, etc)

Definitely want the name and title on the cover. It could be more photography based or design based. A little more abstract. Totally open. Brinewalkers chew up everything they see... One thought was an eaten, old beat up guitar...maybe too cliche.

Album covers i love: Quietfall, Harbour Signals, Ignore All Rhubarb Prophets, Rusted Ladders, Keep Us Warm

Happy to send music or give feedback on concepts prior to working on them...not sure of the rules...whatever is within them.

```html
<!DOCTYPE html>
<html lang="en">
<head>
<meta charset="utf-8">
<title>The Brinewalkers – Nearly Every Road Back Home</title>
<link href="https://fonts.googleapis.com/css2?family=Quicksand:wght@300;400&display=swap" rel="stylesheet">
<style>
  :root {
    --paper: #ffffff;
    --cream: #f6ead9;
    --sun-yellow: #ece53a;
    --ember-red: #e3473f;
    --orange: #ee7a3a;
    --magenta: #b2359a;
    --leaf-green: #3ea22c;
    --ink: #111111;
  }
  html, body {
    margin: 0;
    padding: 0;
    width: 1200px;
    height: 1200px;
    overflow: hidden;
    background: var(--paper);
  }
  .cover {
    position: relative;
    width: 1200px;
    height: 1200px;
    background: var(--paper);
    overflow: hidden;
  }
  .artwork {
    position: absolute;
    pointer-events: none;
  }
  .artwork--warm-splash {
    left: -60px;
    top: -60px;
    width: 820px;
    height: 820px;
    background:
      radial-gradient(ellipse 45% 35% at 35% 35%, var(--sun-yellow) 0%, rgba(236,229,58,0.7) 45%, rgba(236,229,58,0) 75%),
      radial-gradient(ellipse 30% 22% at 58% 45%, var(--ember-red) 0%, rgba(227,71,63,0.7) 50%, rgba(227,71,63,0) 80%),
      radial-gradient(ellipse 22% 30% at 18% 70%, var(--orange) 0%, rgba(238,122,58,0.6) 50%, rgba(238,122,58,0) 80%),
      radial-gradient(ellipse 55% 50% at 40% 40%, var(--cream) 0%, rgba(246,234,217,0) 80%);
    clip-path: polygon(0 0, 100% 0, 95% 30%, 60% 60%, 30% 100%, 0 100%);
  }
  .artwork--violet-stroke-top {
    left: 760px;
    top: 0;
    width: 440px;
    height: 460px;
    background: linear-gradient(200deg, var(--magenta) 0%, rgba(178,53,154,0.85) 55%, rgba(178,53,154,0) 100%);
    clip-path: polygon(55% 0, 100% 0, 100% 35%, 45% 100%, 28% 92%, 48% 45%, 0 40%, 5% 22%, 60% 15%);
  }
  .artwork--green-splatter {
    left: 450px;
    top: 470px;
    width: 750px;
    height: 460px;
    background:
      radial-gradient(ellipse 22% 30% at 20% 40%, var(--leaf-green) 0%, rgba(62,162,44,0.6) 55%, rgba(62,162,44,0) 85%),
      radial-gradient(ellipse 22% 32% at 50% 60%, var(--leaf-green) 0%, rgba(62,162,44,0.6) 55%, rgba(62,162,44,0) 85%),
      radial-gradient(ellipse 18% 28% at 85% 45%, var(--leaf-green) 0%, rgba(62,162,44,0.6) 55%, rgba(62,162,44,0) 85%);
  }
  .artwork--violet-stroke-bottom {
    left: 0;
    top: 830px;
    width: 380px;
    height: 370px;
    background: linear-gradient(30deg, var(--magenta) 0%, rgba(178,53,154,0.9) 60%, rgba(178,53,154,0) 100%);
    clip-path: polygon(0 35%, 80% 0, 100% 20%, 95% 75%, 40% 100%, 0 100%);
  }
  .artwork--green-ridge {
    left: 380px;
    top: 1010px;
    width: 820px;
    height: 190px;
    background:
      radial-gradient(ellipse 30% 70% at 30% 100%, rgba(62,162,44,0.8) 0%, rgba(62,162,44,0) 80%),
      radial-gradient(ellipse 35% 80% at 80% 90%, rgba(62,162,44,0.8) 0%, rgba(62,162,44,0) 80%);
  }
  .title-line {
    position: absolute;
    right: 27px;
    top: 948px;
    margin: 0;
    font-family: "Quicksand", sans-serif;
    font-weight: 300;
    font-size: 43px;
    letter-spacing: 1px;
    line-height: 1;
    color: var(--ink);
    white-space: nowrap;
  }
</style>
</head>
<body>
  <main class="cover">
    <div class="artwork artwork--warm-splash" role="img" aria-label="Yellow, red and orange paint splashes with shards and small flying birds"></div>
    <div class="artwork artwork--violet-stroke-top" role="img" aria-label="Broad magenta brush strokes with dark birds in flight and ink drops"></div>
    <div class="artwork artwork--green-splatter" role="img" aria-label="Textured green paint splatter with black ink blots"></div>
    <div class="artwork artwork--violet-stroke-bottom" role="img" aria-label="Magenta brush stroke with a black ink blot"></div>
    <div class="artwork artwork--green-ridge" role="img" aria-label="Green painted ridges with grey birds flying low"></div>
    <h1 class="title-line">the brinewalkers/nearly every road back home</h1>
  </main>
</body>
</html>
```